Product label design needed for an odor removal line of products.

I need a label designed for an odor removal product line. There are eight additional odor removal products that I will need labels designed for so the winner will have additional work from me. I would like each of those products to have a similar look and feel in each one. This contest is for one of the products. The Breezeward Pod 385 (would love a better name if you are so inclined -many people know what it is by the 385). The no smell formula does not mask odors, it eliminates odors at their source . Also Reduces Allergens! Simply open silver packet and place in dispenser. Great for use in cars, near pet beds or litter boxes, near diaper pails -anywhere odors are a problem. Lasts 60-90 days. Safe to use. Other uses: Nursing homes, hotel rooms, locker rooms, teenage boy rooms, basements... Eco Friendly! No VOC's or phthalates! Do not consume. Keep out of reach of children and pets. Replace every 60-90 days. I put the picture of my logo , the product as it is packaged and a picture of the actual product and the dispenser it will go in. the package is 4x5 in silver packet with .25 seam on the side and .5 seam on the top and bottom. (Dispenser will have a label with reorder information on it. to be designed later) You do not have to put all information provided on the label. It is to be used as you see fit. I tend to like clean, bold designs but am open to all options. Prefer not to use word air freshener.

Target Market(s)

Men and women between 30-65

Industry/Entity Type

Cleaning Product

Font styles to use
Sans Serif

Colors
acd136
9bcb3c
ffffff

Requirements
Must have
• ability for concept/look to be used for a laundry product, smaller odor elimination pouch, odor removing canister and spray as well
Nice to have
• I like greens but am open to designers to decide
Should not have
• word air freshener

```html
<!DOCTYPE html>
<html lang="en">
<head>
<meta charset="UTF-8">
<title>The Breezeward Pod 385 – Pouch Label</title>
<link href="https://fonts.googleapis.com/css2?family=Montserrat:wght@800;900&family=Barlow:wght@500;600&display=swap" rel="stylesheet">
<style>
  :root {
    --backdrop: #efefef;
    --silver-light: #e4e4e4;
    --silver-mid: #bdbdbd;
    --silver-dark: #9a9a9a;
    --panel-gray: #5c5c5c;
    --title-gray: #4d4d4d;
    --strip-gray: #4a4a4a;
    --green: #9bcb3c;
    --green-light: #acd136;
    --green-seam: #86b532;
    --white: #ffffff;
  }
  * { margin: 0; padding: 0; box-sizing: border-box; }
  html, body { width: 1200px; height: 900px; overflow: hidden; }
  body {
    background: var(--backdrop);
    display: flex;
    align-items: center;
    justify-content: center;
  }
  .pouch-label {
    position: relative;
    width: 560px;
    height: 700px;
    background: linear-gradient(100deg, var(--silver-mid) 0%, var(--silver-light) 22%, var(--silver-dark) 48%, var(--silver-light) 75%, var(--silver-mid) 100%);
    overflow: hidden;
  }
  .seam-top {
    position: absolute; left: 0; top: 0; width: 100%; height: 40px;
    background: repeating-linear-gradient(180deg, #d6d6d6 0 3px, #a8a8a8 3px 5px);
  }
  .brand-panel {
    position: absolute; left: 90px; top: 60px; width: 380px; height: 250px;
    background: var(--panel-gray);
    display: flex; align-items: center; justify-content: center; gap: 18px;
  }
  .brand-dot {
    width: 64px; height: 64px; border-radius: 50%;
    background: var(--green);
  }
  .brand-name {
    font-family: "Montserrat", sans-serif;
    font-weight: 800;
    font-size: 34px;
    line-height: 1.1;
    color: var(--green);
    text-transform: uppercase;
  }
  .product-title {
    position: absolute; left: 0; top: 335px; width: 100%;
    text-align: center;
    font-family: "Montserrat", sans-serif;
    font-weight: 900;
    font-size: 46px;
    line-height: 1.2;
    color: var(--title-gray);
    text-transform: uppercase;
  }
  .claim-strip {
    position: absolute; left: 0; top: 468px; width: 100%; height: 40px;
  }
  .claim-strip svg { position: absolute; inset: 0; }
  .claim-text {
    position: relative;
    display: flex; align-items: center; justify-content: center; height: 100%;
    font-family: "Barlow", sans-serif; font-weight: 600; font-size: 17px;
    color: var(--white);
  }
  .care-band {
    position: absolute; left: 0; top: 508px; width: 100%; height: 152px;
    background: linear-gradient(180deg, var(--green-light), var(--green));
    display: flex; justify-content: center; align-items: flex-start;
    padding-top: 28px;
    font-family: "Barlow", sans-serif; font-weight: 500; font-size: 22px;
    line-height: 1.15; color: var(--white);
  }
  .care-note { padding: 0 20px; }
  .care-note--left { text-align: right; border-right: 2px solid var(--white); }
  .care-note--right { text-align: left; }
  .seam-bottom {
    position: absolute; left: 0; bottom: 0; width: 100%; height: 40px;
    background: repeating-linear-gradient(180deg, var(--green) 0 3px, var(--green-seam) 3px 5px);
  }
</style>
</head>
<body>
  <main class="pouch-label">
    <div class="seam-top"></div>

    <div class="brand-panel">
      <span class="brand-dot"></span>
      <span class="brand-name">Verdant<br>Haven</span>
    </div>

    <h1 class="product-title">The Breezeward<br>Pod 385</h1>

    <div class="claim-strip">
      <svg width="560" height="40" viewBox="0 0 560 40" aria-hidden="true">
        <polygon points="40,0 520,0 500,40 60,40" fill="var(--strip-gray)"/>
      </svg>
      <p class="claim-text">Eco Friendly! &nbsp;| No VOC's or phthalates!</p>
    </div>

    <section class="care-band">
      <p class="care-note care-note--left">Keep out of reach of<br>children and pets.</p>
      <p class="care-note care-note--right">Replace every<br>60-90 days</p>
    </section>

    <div class="seam-bottom"></div>
  </main>
</body>
</html>
```